Harrowgate Construction And Masonry Ltd

Black background

Logo - attached

Services (bullet points)
New Builds
Extensions
Refurbishments
Alterations
Brickwork Specialists

Contact details - 01632 960418 or 0791 5530274

Email address - contact@harrowgateconstructionandmasonry.co.uk

Website - www.harrowgateconstructionandmasonry.co.uk

Facebook logo

```html
<!DOCTYPE html>
<html lang="en">
<head>
<meta charset="utf-8">
<title>Harrowgate Construction And Masonry Ltd – Flyer</title>
<link href="https://fonts.googleapis.com/css2?family=Kumbh+Sans:wght@400;500;600;700&display=swap" rel="stylesheet">
<style>
  :root {
    --backdrop: #dcdedd;
    --ink: #070808;
    --green: #3dba63;
    --white: #ffffff;
    --photo-warm: #b58a4c;
    --photo-grey: #8a8d8c;
    --photo-light: #d9d6cf;
  }
  * { box-sizing: border-box; margin: 0; padding: 0; }
  html, body { width: 902px; height: 1200px; overflow: hidden; background: var(--backdrop); }
  body { font-family: "Kumbh Sans", sans-serif; color: var(--white); }

  .flyer {
    position: absolute; left: 27px; top: 0;
    width: 848px; height: 1200px;
    background: var(--ink); overflow: hidden;
  }
  .frame-line { position: absolute; background: var(--green); }
  .frame-line.vertical { left: 54px; top: 298px; width: 2px; height: 852px; }
  .frame-line.horizontal { left: 54px; top: 1148px; width: 742px; height: 2px; }

  .brand { position: absolute; left: 78px; top: 70px; width: 204px; text-align: center; }
  .brand-mark { width: 60px; height: 60px; border-radius: 50%; background: var(--green); margin: 14px auto 22px; }
  .brand-name { font-weight: 600; font-size: 25px; letter-spacing: 0.5px; line-height: 1; color: var(--white); }
  .brand-sub { font-weight: 600; font-size: 9.2px; line-height: 1; margin-top: 8px; color: var(--white); letter-spacing: 0.1px; }

  .headline { position: absolute; left: 76px; top: 285px; font-weight: 600; font-size: 71px; line-height: 83px; letter-spacing: -0.5px; }
  .headline .accent { color: var(--green); }

  .intro { position: absolute; left: 78px; top: 555px; width: 545px; font-weight: 500; font-size: 15.3px; line-height: 23.3px; }

  .services-tag {
    position: absolute; left: 74px; top: 690px; width: 222px; height: 39px;
    background: var(--green); border-radius: 22px 22px 0 22px;
    font-weight: 600; font-size: 32px; line-height: 41px; padding-left: 22px; color: var(--white);
  }
  .services { position: absolute; left: 84px; top: 746px; list-style: none; }
  .services li { display: flex; align-items: center; height: 31.7px; font-weight: 500; font-size: 27px; }
  .services svg { width: 22px; height: 22px; margin-right: 13px; flex: none; }

  .gallery-deco { position: absolute; left: 0; top: 0; width: 848px; height: 1200px; }
  .photo {
    position: absolute; border: 6px solid var(--white);
    box-shadow: 0 3px 8px rgba(0,0,0,0.5);
  }
  .photo.kitchen-dark { left: 563px; top: 659px; width: 155px; height: 120px; transform: rotate(-15deg);
    background: linear-gradient(160deg, var(--photo-light), var(--photo-grey) 60%, #5b5f60); }
  .photo.roof-frame { left: 519px; top: 779px; width: 142px; height: 126px; transform: rotate(8deg);
    background: linear-gradient(135deg, #7fa7d4, var(--photo-warm) 45%, #6b4a22); }
  .photo.kitchen-bright { left: 604px; top: 887px; width: 142px; height: 142px; transform: rotate(-8deg);
    background: linear-gradient(170deg, #eeeeea, var(--photo-light) 50%, #7a5b3e); }

  .call-tag {
    position: absolute; left: 78px; top: 1031px; width: 145px; height: 23px;
    background: var(--green); border-radius: 12px 12px 0 12px;
    font-weight: 600; font-size: 12.5px; line-height: 24px; text-align: center; color: var(--white);
  }
  .social { position: absolute; left: 239px; top: 1030px; display: flex; gap: 8px; }
  .social span { width: 24px; height: 24px; border: 2.5px solid var(--green); border-radius: 50%; }

  .phones { position: absolute; left: 78px; top: 1060px; font-weight: 600; font-size: 30px; line-height: 32px; letter-spacing: 1px; }

  .web-contacts { position: absolute; right: 75px; top: 1079px; text-align: right; font-weight: 500; font-size: 12.6px; }
  .web-contacts p { display: flex; align-items: center; justify-content: flex-end; height: 25px; }
  .web-contacts svg { width: 16px; height: 16px; margin-left: 10px; }
</style>
</head>
<body>
<main class="flyer">
  <div class="frame-line vertical"></div>
  <div class="frame-line horizontal"></div>

  <header class="brand">
    <div class="brand-mark"></div>
    <div class="brand-name">HARROWGATE</div>
    <div class="brand-sub">CONSTRUCTION AND MASONRY LTD</div>
  </header>

  <h1 class="headline">Building<br>and Brickwork<br><span class="accent">Specialist’s</span></h1>

  <p class="intro">Harrowgate Construction and Masonry offer the complete building service with over 15 years experience working throughout Cambridgeshire with local home owners looking to improve and add value to their properties.</p>

  <div class="services-tag">SERVICES</div>
  <ul class="services">
    <li><svg viewBox="0 0 22 22"><rect x="2" y="4" width="15" height="15" rx="3" fill="none" stroke="#3dba63" stroke-width="2.2"/><path d="M6 11l4 4 10-11" fill="none" stroke="#3dba63" stroke-width="2.4" stroke-linecap="round" stroke-linejoin="round"/></svg>New Builds</li>
    <li><svg viewBox="0 0 22 22"><rect x="2" y="4" width="15" height="15" rx="3" fill="none" stroke="#3dba63" stroke-width="2.2"/><path d="M6 11l4 4 10-11" fill="none" stroke="#3dba63" stroke-width="2.4" stroke-linecap="round" stroke-linejoin="round"/></svg>Extensions</li>
    <li><svg viewBox="0 0 22 22"><rect x="2" y="4" width="15" height="15" rx="3" fill="none" stroke="#3dba63" stroke-width="2.2"/><path d="M6 11l4 4 10-11" fill="none" stroke="#3dba63" stroke-width="2.4" stroke-linecap="round" stroke-linejoin="round"/></svg>Refurbishments</li>
    <li><svg viewBox="0 0 22 22"><rect x="2" y="4" width="15" height="15" rx="3" fill="none" stroke="#3dba63" stroke-width="2.2"/><path d="M6 11l4 4 10-11" fill="none" stroke="#3dba63" stroke-width="2.4" stroke-linecap="round" stroke-linejoin="round"/></svg>Alterations</li>
    <li><svg viewBox="0 0 22 22"><rect x="2" y="4" width="15" height="15" rx="3" fill="none" stroke="#3dba63" stroke-width="2.2"/><path d="M6 11l4 4 10-11" fill="none" stroke="#3dba63" stroke-width="2.4" stroke-linecap="round" stroke-linejoin="round"/></svg>Brickwork Specialists</li>
  </ul>

  <svg class="gallery-deco" viewBox="0 0 848 1200" aria-hidden="true">
    <circle cx="729" cy="783" r="55" fill="none" stroke="#3dba63" stroke-width="14"/>
    <circle cx="527" cy="724" r="11" fill="#3dba63"/>
    <circle cx="788" cy="936" r="19" fill="#3dba63"/>
    <g stroke="#3dba63" stroke-width="1.6">
      <line x1="725" y1="701" x2="759" y2="668"/>
      <line x1="760" y1="897" x2="774" y2="883"/>
      <line x1="529" y1="999" x2="569" y2="960"/>
    </g>
  </svg>
  <div class="photo kitchen-dark" role="img" aria-label="Photo of a finished grey fitted kitchen with bar stools"></div>
  <div class="photo roof-frame" role="img" aria-label="Photo of timber roof joists under construction"></div>
  <div class="photo kitchen-bright" role="img" aria-label="Photo of a bright open-plan kitchen extension with skylights"></div>

  <div class="call-tag">CALL NOW TODAY!</div>
  <div class="social"><span></span><span></span></div>
  <div class="phones">01632 960418<br>0791 5530274</div>

  <div class="web-contacts">
    <p>contact@harrowgateconstructionandmasonry.co.uk<svg viewBox="0 0 16 16"><rect x="1.5" y="3" width="13" height="10" rx="1.5" fill="none" stroke="#3dba63" stroke-width="1.3"/><path d="M2 4l6 5 6-5" fill="none" stroke="#3dba63" stroke-width="1.3"/></svg></p>
    <p>www.harrowgateconstructionandmasonry.co.uk<svg viewBox="0 0 16 16"><circle cx="8" cy="8" r="6.5" fill="none" stroke="#3dba63" stroke-width="1.3"/><ellipse cx="8" cy="8" rx="3" ry="6.5" fill="none" stroke="#3dba63" stroke-width="1.1"/><line x1="1.5" y1="8" x2="14.5" y2="8" stroke="#3dba63" stroke-width="1.1"/></svg></p>
  </div>
</main>
</body>
</html>
```